Business Card Design Competition

We need a business card design for our Internet Marketing company. We require both front and back designs and the final card must be 89x53mm in size, plus crop marks to 91x55mm. Colours as per logo, plus perhaps black and/or grey (#828282).
Final text must be editable (if you can supply an editable Fireworks PNG, even better)...
FRONT TEXT:
Full Name
Position
Address Line
Suburb, State, Postcode
Phone: 0000 000 000
Mobile: 0000 000 000
Email: xxx@brimleafpromo.com.au
Web: www.brimleafpromo.com.au
Rear of card should be a fresh design plus our slogan text: "Making You Memorable" in large font, then in small text "Brimleaf Holdings Pty Ltd (ABN: 42 563 701 384)".
Target Market(s)
Small/Medium Businesses
Industry/Entity Type
Business
Look and feel
Each slider illustrates characteristics of the customer's brand and the style your logo design should communicate.

```html
<!DOCTYPE html>
<html lang="en">
<head>
<meta charset="utf-8">
<title>Brimleaf Promo – Business Card</title>
<link rel="stylesheet" href="https://fonts.googleapis.com/css2?family=Roboto+Condensed:wght@400&family=Great+Vibes&display=swap">
<style>
  :root {
    --orange: #f7a42d;
    --green: #95c63e;
    --grey: #828282;
    --border: #9a9a9a;
    --peach-soft: #fdeedb;
    --peach-text: #fde0b4;
    --white: #ffffff;
  }
  html, body {
    margin: 0;
    padding: 0;
    width: 1200px;
    height: 901px;
    overflow: hidden;
    background: var(--white);
  }
  .sheet {
    position: relative;
    width: 1200px;
    height: 901px;
  }
  .card {
    position: absolute;
    left: 293px;
    width: 666px;
    height: 396px;
    box-sizing: border-box;
    overflow: hidden;
    font-family: "Roboto Condensed", "Arial Narrow", sans-serif;
  }
  .card--front {
    top: 41px;
    background: var(--white);
    border: 1px solid var(--border);
  }
  .card--back {
    top: 491px;
    background: var(--orange);
  }
  .decor-area {
    position: absolute;
    left: 0;
    bottom: 0;
    width: 380px;
    height: 300px;
  }
  .card--front .decor-area {
    background: radial-gradient(circle at 0% 100%, var(--peach-soft) 0%, rgba(253,238,219,0.6) 55%, rgba(253,238,219,0) 80%);
  }
  .card--back .decor-area {
    background: radial-gradient(circle at 0% 100%, var(--green) 0%, rgba(149,198,62,0.75) 55%, rgba(149,198,62,0) 82%);
  }
  .contact {
    position: absolute;
    left: 37px;
    top: 86px;
    color: var(--grey);
  }
  .contact__name {
    margin: 0;
    font-size: 22px;
    font-weight: 400;
    line-height: 26px;
  }
  .contact__role {
    margin: 0 0 32px;
    font-size: 11px;
    line-height: 12px;
  }
  .contact__group {
    margin: 0 0 27px;
    font-size: 19.5px;
    line-height: 26px;
  }
  .brand {
    position: absolute;
    left: 330px;
    top: 44px;
    display: flex;
    align-items: center;
    gap: 12px;
  }
  .brand__dot {
    width: 86px;
    height: 86px;
    border-radius: 50%;
    background: var(--green);
  }
  .brand__name {
    font-size: 32px;
    line-height: 1;
    color: var(--orange);
    font-weight: 400;
  }
  .slogan {
    position: absolute;
    left: 316px;
    top: 42px;
    margin: 0;
    font-family: "Great Vibes", cursive;
    font-size: 38px;
    font-weight: 400;
    color: var(--white);
  }
  .legal {
    position: absolute;
    right: 22px;
    bottom: 14px;
    margin: 0;
    text-align: right;
    color: var(--peach-text);
    font-size: 17.5px;
    line-height: 23px;
  }
</style>
</head>
<body>
<main class="sheet">
  <section class="card card--front" aria-label="Card front">
    <div class="decor-area" role="img" aria-label="Faint brand decoration area"></div>
    <div class="contact">
      <p class="contact__name">Daniel Harrow</p>
      <p class="contact__role">Founder and CEO</p>
      <p class="contact__group">Tel.&nbsp;&nbsp; 1300 555 014<br>Mob. 0400 555 777</p>
      <p class="contact__group">48 Wattle Lane<br>Ballarat Vic 3350</p>
      <p class="contact__group">daniel@brimleafpromo.com.au<br>www.brimleafpromo.com.au</p>
    </div>
    <div class="brand">
      <span class="brand__dot"></span>
      <span class="brand__name">Brimleaf Promo</span>
    </div>
  </section>

  <section class="card card--back" aria-label="Card back">
    <div class="decor-area" role="img" aria-label="Large brand decoration area"></div>
    <p class="slogan">Making You Memorable</p>
    <p class="legal">Brimleaf Holdings Pty Ltd<br>ABN: 42 563 701 384</p>
  </section>
</main>
</body>
</html>
```